Product labels for new supplements business targeting high performing creative people

I need a label design for different supplements like Whey, BCAA, Melatonin etc. that I could customize for each use case separately.

The brand is called lanternfolk.life, and it would be the first design of the labels. We haven't sold any products yet, but the target audience is people with growth mindset, people who want to be as efficient as possible and are constantly looking to improve their lifestyle. As part of that, they are also working out, but don't know much about supplements yet. Mostly people between 20-34.

I don't have a too specific idea of the expected design, though it should be light, warm, smart and minimalist, maybe have some patterns. It should looks smart and clean (and expensive). Orange and golden might be the additional colors for white. I have attached the templates of some products that I plan to sell and also the logo of the brand.

Here's what I have used for inspiration:
Brands that I like and are somewhat similar in concept: https://www.vimqera.com/ (!!specially the way they
bring "how the product helps them" in focus, not "what the product is" & https://www.pobri.care/ &
https://www.selvoda.com/sport/ & https://en.kambelo.fr/ &
https://gridmarket.com/profiles/corawellhaldesign/designs/417586

Here's how different products look like: https://prodaxel.com/catalog

Target Market(s)

target audience is people with growth mindset, people who want to be as efficient as possible and are constantly looking to improve their lifestyle. As part of that, they are also working out, but don't know much about supplements yet. Mostly people between 20-34.

Industry/Entity Type

Supplements

Font styles to use
Sans Serif

Colors
FFC000
F8CF3A
FAE287
FDF2CF
FEFAEE
F0912C
F2A743
F7CA91
FBE8D2
FDF5EE
EE7325
F08F49
F5BC92
FAE3D3
FDF4ED

Requirements
Must have
• Clean, smart and minimalist design that can be applied for different products in different sizes, like Whey protein, BCAA, vitamins etc. available here: https://prodaxel.com/catalog
Nice to have
• Patterns, expensive look
Should not have
• Doodles, too many colors

```html
<!DOCTYPE html>
<html lang="en">
<head>
<meta charset="utf-8">
<title>lanternfolk.life — Supplement Labels</title>
<link href="https://fonts.googleapis.com/css2?family=Montserrat:wght@300;400;500&family=Poppins:wght@300;400;500;600&family=Arimo:wght@400;700&display=swap" rel="stylesheet">
<style>
  :root {
    --backdrop: #F2EDB6;
    --paper: #FFFFFF;
    --ink: #222222;
    --ink-soft: #555555;
    --gold: #FFC000;
    --gold-soft: #F8CF3A;
    --gold-pale: #FAE287;
    --cream: #FDF2CF;
    --orange: #F0912C;
    --brand-dot: #EE7325;
    --marker: #C0504D;
  }
  * { box-sizing: border-box; margin: 0; padding: 0; }
  html, body { width: 1200px; height: 1012px; overflow: hidden; }
  body {
    background: var(--backdrop);
    position: relative;
    font-family: "Poppins", sans-serif;
    color: var(--ink);
  }

  /* shared brand pieces */
  .brand { display: flex; align-items: center; gap: 6px; font-family: "Poppins", sans-serif; font-weight: 500; color: var(--ink); position: absolute; }
  .brand-dot { width: 10px; height: 10px; border-radius: 50%; background: var(--brand-dot); }
  .wave-band { position: absolute; left: 0; right: 0; bottom: 0; background: linear-gradient(180deg, rgba(255,255,255,0) 0%, var(--cream) 35%, var(--gold-pale) 70%, var(--cream) 100%); }
  .seal-mark { position: absolute; border-radius: 50%; background: radial-gradient(circle, var(--gold-pale) 0%, var(--cream) 70%); opacity: .8; }

  .product-title { position: absolute; font-family: "Montserrat", sans-serif; font-weight: 300; line-height: 1; }
  .product-title .line-main { display: block; color: var(--ink); }
  .product-title .line-accent { display: block; color: var(--gold); }
  .product-title .line-flavor { display: block; color: var(--ink-soft); }
  .product-title .ratio { color: var(--gold); }

  .product-meta { position: absolute; font-family: "Montserrat", sans-serif; color: var(--ink); }
  .product-meta .kind { font-weight: 400; letter-spacing: .02em; }
  .product-meta .weight { font-weight: 300; color: var(--ink-soft); }

  /* front panels */
  .front-panel { position: absolute; top: 34px; width: 290px; height: 420px; background: var(--paper); box-shadow: 0 6px 18px rgba(120,110,40,.18); overflow: hidden; }
  .front-panel .brand { left: 22px; top: 26px; font-size: 15px; }
  .front-panel .wave-band { height: 40px; }
  .front-panel .product-title .line-main, .front-panel .product-title .line-accent { font-size: 38px; }
  .front-panel .product-title .line-flavor { font-size: 21px; margin-top: 4px; }
  .front-panel .product-meta { left: 24px; bottom: 54px; }
  .front-panel .product-meta .kind { font-size: 11.5px; }
  .front-panel .product-meta .weight { font-size: 11px; margin-top: 8px; }

  .panel-one { left: 110px; }
  .panel-one .product-title { left: 24px; top: 100px; }
  .panel-one .seal-mark { left: 26px; top: 288px; width: 28px; height: 28px; }

  .panel-two { left: 470px; }
  .panel-two .product-title { left: 24px; top: 200px; }
  .panel-two .seal-mark { left: 16px; top: 180px; width: 40px; height: 40px; }

  .panel-bcaa { left: 830px; }
  .panel-bcaa .product-title { left: 20px; top: 196px; }
  .panel-bcaa .product-title .line-main { font-size: 36px; }
  .panel-bcaa .product-title .line-flavor { font-size: 21px; }
  .panel-bcaa .seal-mark { left: 14px; top: 178px; width: 40px; height: 40px; }

  .version-marker { position: absolute; top: 226px; font-family: "Poppins", sans-serif; font-weight: 300; font-size: 26px; color: var(--marker); }
  .marker-one { left: 78px; }
  .marker-two { left: 438px; }

  /* flat wrap label */
  .wrap-label { position: absolute; left: 50px; top: 500px; width: 1100px; height: 460px; background: var(--paper); box-shadow: 0 6px 18px rgba(120,110,40,.18); overflow: hidden; }
  .wrap-label .wave-band { height: 36px; }
  .wrap-label .corner-wave { position: absolute; left: 0; top: 0; width: 80px; height: 70px; background: radial-gradient(ellipse at 0 30%, var(--gold-pale) 0%, var(--cream) 55%, rgba(255,255,255,0) 80%); }

  .info-column { position: absolute; left: 28px; top: 42px; width: 310px; font-size: 12.3px; line-height: 1.35; color: #333; font-weight: 300; }
  .info-column p { margin-bottom: 16px; }
  .info-column .heading { color: var(--gold); font-weight: 600; font-size: 11.5px; margin-bottom: 0; letter-spacing: .02em; }
  .info-column .fine { font-size: 9.6px; line-height: 1.35; margin-bottom: 12px; }

  .wrap-label .brand { left: 410px; top: 32px; font-size: 17px; }
  .wrap-label .seal-mark { left: 378px; top: 210px; width: 48px; height: 48px; }
  .wrap-label .product-title { left: 405px; top: 232px; }
  .wrap-label .product-title .line-main, .wrap-label .product-title .line-accent { font-size: 39px; }
  .wrap-label .product-title .line-flavor { font-size: 22px; margin-top: 2px; }
  .wrap-label .product-meta { left: 406px; top: 376px; }
  .wrap-label .product-meta .kind { font-size: 12px; }
  .wrap-label .product-meta .weight { font-size: 12px; margin-top: 10px; }

  .facts-panel { position: absolute; left: 754px; top: 44px; width: 320px; border: 2px solid #000; padding: 2px 4px 6px; font-family: "Arimo", sans-serif; font-size: 11px; color: #000; }
  .facts-title { font-weight: 700; font-size: 30px; line-height: 1.05; letter-spacing: -.01em; }
  .facts-serving { margin: 4px 0 2px 2px; line-height: 1.15; }
  .facts-table { width: 100%; border-collapse: collapse; }
  .facts-table th { font-weight: 700; font-size: 10.5px; text-align: right; line-height: 1.05; padding: 4px 0 2px; border-top: 8px solid #000; border-bottom: 4px solid #000; vertical-align: bottom; }
  .facts-table td { padding: 3px 2px 2px; border-bottom: 1px solid #000; }
  .facts-table td.amount { text-align: right; }
  .facts-table td.dv { text-align: right; width: 50px; }
  .facts-table tr.last td { border-bottom: 4px solid #000; }
  .facts-note { margin-top: 8px; padding-left: 2px; }
  .other-ingredients { position: absolute; left: 762px; top: 244px; width: 310px; font-family: "Arimo", sans-serif; font-size: 11.5px; line-height: 1.2; color: #000; }
  .maker-block { position: absolute; left: 762px; top: 362px; font-family: "Poppins", sans-serif; font-size: 9.5px; line-height: 1.35; color: #222; font-weight: 500; }
</style>
</head>
<body>

  <span class="version-marker marker-one">1</span>
  <section class="front-panel panel-one" aria-label="Front label, version 1">
    <div class="brand"><span class="brand-dot"></span>lanternfolk.life</div>
    <h1 class="product-title"><span class="line-main">PROTEINE</span><span class="line-accent">SHAKE</span><span class="line-flavor">CHOCOLATE</span></h1>
    <div class="seal-mark" role="img" aria-label="Small golden line-pattern seal"></div>
    <div class="product-meta"><div class="kind">DIETARY SUPPLEMENT</div><div class="weight">Net Wt. 300 g (10.58oz)</div></div>
    <div class="wave-band" role="img" aria-label="Golden wavy line pattern band"></div>
  </section>

  <span class="version-marker marker-two">2</span>
  <section class="front-panel panel-two" aria-label="Front label, version 2">
    <div class="brand"><span class="brand-dot"></span>lanternfolk.life</div>
    <div class="seal-mark" role="img" aria-label="Small golden line-pattern seal"></div>
    <h1 class="product-title"><span class="line-main">PROTEINE</span><span class="line-accent">SHAKE</span><span class="line-flavor">CHOCOLATE</span></h1>
    <div class="product-meta"><div class="kind">DIETARY SUPPLEMENT</div><div class="weight">Net Wt. 300 g (10.58oz)</div></div>
    <div class="wave-band" role="img" aria-label="Golden wavy line pattern band"></div>
  </section>

  <section class="front-panel panel-bcaa" aria-label="Front label, BCAA wild berry">
    <div class="brand"><span class="brand-dot"></span>lanternfolk.life</div>
    <div class="seal-mark" role="img" aria-label="Small golden line-pattern seal"></div>
    <h1 class="product-title"><span class="line-main">BCAA <span class="ratio">2:1:1</span></span><span class="line-flavor">WILD BERRY</span></h1>
    <div class="product-meta"><div class="kind">DIETARY SUPPLEMENT</div><div class="weight">Net Wt. 300 g (10.58oz)</div></div>
    <div class="wave-band" role="img" aria-label="Golden wavy line pattern band"></div>
  </section>

  <section class="wrap-label" aria-label="Full wrap-around label">
    <div class="corner-wave" role="img" aria-label="Golden wavy line pattern corner"></div>

    <div class="info-column">
      <p>80% protein, with A, B1, B2, B3, B6, B12, and C. Protein promotes muscle gain and helps maintain muscle mass.*</p>
      <p class="heading">SUGGESTED USE:</p>
      <p>As a dietary supplement take 1 (one) tablet 15-30 minutes before bed or as directed by your healthcare professional.</p>
      <p class="heading">CAUTION:</p>
      <p>Do not exceed recommended dose. Pregnant or nursing mothers, children under the age of 18, and individuals with a known medical condition should consult a physician before using this or any dietary supplement.</p>
      <p class="fine">KEEP OUT OF REACH OF CHILDREN. DO NOT USE IF SAFETY SEAL IS DAMAGED OR MISSING. STORE IN A COOL, DRY PLACE.</p>
      <p class="fine">* These statements have not been evaluated by the Food and Drug Administration. This product is not intended to diagnose, treat, cure or prevent any disease.</p>
    </div>

    <div class="brand"><span class="brand-dot"></span>lanternfolk.life</div>
    <div class="seal-mark" role="img" aria-label="Small golden line-pattern seal"></div>
    <h1 class="product-title"><span class="line-main">PROTEINE</span><span class="line-accent">SHAKE</span><span class="line-flavor">CHOCOLATE</span></h1>
    <div class="product-meta"><div class="kind">DIETARY SUPPLEMENT</div><div class="weight">Net Wt. 300 g (10.58oz)</div></div>

    <div class="facts-panel">
      <div class="facts-title">Supplement Facts</div>
      <div class="facts-serving">Serving Size: 1 tablet<br>Servings per container: 60</div>
      <table class="facts-table">
        <tr><th></th><th>Amount per<br>Serving</th><th>% Daily<br>Value</th></tr>
        <tr><td>Calories</td><td class="amount">0.076 Kcal</td><td class="dv">*</td></tr>
        <tr class="last"><td>Melatonin</td><td class="amount">1000 µg</td><td class="dv">*</td></tr>
      </table>
      <div class="facts-note">*Daily Value not established.</div>
    </div>
    <p class="other-ingredients">Other Ingredients: Microcrystalline cellulose, starch, magnesium salts of fatty acids and silica.</p>
    <p class="maker-block">Manufactured for and distributed by:<br>[your LLC name here]<br>Address:<br>[your legal address and phone nr or email]</p>

    <div class="wave-band" role="img" aria-label="Golden wavy line pattern band"></div>
  </section>

</body>
</html>
```